Glenmorrow ice cream tub packaging

We need new tub designs for our dairy free ice cream. It is made with avocado and coconut which we would like communicated within the design. We launched last year and have had positive feedback regarding our current packaging but also that it could be a cleaner design with a more sophisticated font as it will be sold in more high end expensive stores. I have attached our current packaging for info (there are 3 flavours - Original Avocado, Raspberry and Basil, Raw Cacao) We would like to keep the avocado print that is currently included on the packaging as we have had a lot of very positive feedback about that. Maybe not as much though as it makes it quite busy and we prefer a clean design.
I've also attached our new logo.
We would like it to mention we are gluten, soya, dairy, egg and nut free. And that it is a 'coconut and avocado ice cream' rather than an 'alternative'.
The nutritional label needs to be in a UK table format (I've attached a blank copy for information). We don't currently have the values for the table as it has been sent off for testing as we have a new recipe. But if you could leave that blank we will fill it in when we have the results.
I've attached the template for the sizes as we have two sizes - 500ml and 100ml. The designs will be the same but just smaller/bigger. It has to be font size 11 for legal purpose.
It has to have the weight (100ml and 500ml) followed by the official e-mark.
The ingredients are the same but take out Locust Bean Gum and replace Vanilla extract with Lime Juice.
The business address is the same but should read 'Glenmorrow LTD'. All other info on the packaging (barcode, text etc) is to remain the same.
I've have also attached 3 pictures of other tub designs that we like for inspiration - our favourite is 'zelt' as we can have half the print half the colour if the flavour (raspberry/pink, cacao/brown, original/green)
Updates
Target Market(s)
High end health food stores
Look and feel

```html
<!DOCTYPE html>
<html lang="en">
<head>
<meta charset="utf-8">
<title>Glenmorrow Tub Packaging – Original Avocado</title>
<link rel="stylesheet" href="https://fonts.googleapis.com/css2?family=Barlow+Condensed:ital,wght@0,300;0,400;0,500;1,500&family=Old+Standard+TT:wght@400;700&display=swap">
<style>
  :root {
    --backdrop: #e4e4e4;
    --leaf: #8cc63f;
    --leaf-deep: #5f8a2a;
    --print-lid: #d6f79c;
    --print-wrap: #eef8c4;
    --panel-soft: #ccfd93;
    --white: #ffffff;
    --ink: #111111;
    --cocoa: #6b3d12;
    --terracotta: #b0513f;
  }
  * { margin: 0; padding: 0; box-sizing: border-box; }
  html, body { width: 1200px; height: 1200px; overflow: hidden; }
  body {
    background: var(--backdrop);
    position: relative;
    font-family: "Barlow Condensed", sans-serif;
  }
  .artwork { position: absolute; inset: 0; width: 1200px; height: 1200px; }

  .label-card {
    position: absolute;
    background: var(--white);
    text-align: center;
    display: flex;
    flex-direction: column;
    align-items: center;
  }
  .product-title {
    font-style: italic;
    font-weight: 500;
    color: var(--ink);
    line-height: 1;
  }
  .rule { background: var(--leaf); height: 2px; border-radius: 2px; }
  .brand {
    display: flex; align-items: center;
    font-weight: 500; color: var(--leaf-deep);
    letter-spacing: 0.04em; line-height: 1;
  }
  .brand-dot { border-radius: 50%; background: var(--leaf); flex: none; }
  .tagline { color: var(--terracotta); font-weight: 400; line-height: 1; }
  .claims { color: var(--cocoa); font-weight: 300; line-height: 1.2; }

  /* Lid */
  .lid-card { left: 424px; top: 150px; width: 346px; height: 346px; border-radius: 24px; padding-top: 26px; }
  .lid-card .product-title { font-size: 29px; }
  .lid-card .rule { width: 200px; margin: 10px 0 18px; }
  .lid-card .brand { font-size: 46px; gap: 10px; }
  .lid-card .brand-dot { width: 14px; height: 14px; }
  .lid-card .tagline { font-size: 24px; margin-top: 8px; }
  .lid-card .rule.lower { margin: 16px 0 14px; }
  .lid-card .claims { font-size: 27px; }

  /* Wrap front */
  .front-frame {
    position: absolute; left: 480px; top: 734px; width: 224px; height: 222px;
    background: var(--panel-soft); border-radius: 16px;
  }
  .front-card { left: 502px; top: 756px; width: 180px; height: 178px; border-radius: 14px; padding-top: 14px; }
  .front-card .product-title { font-size: 14px; }
  .front-card .brand { font-size: 24px; gap: 5px; margin-top: 8px; }
  .front-card .brand-dot { width: 7px; height: 7px; }
  .front-card .tagline { font-size: 12.5px; margin-top: 5px; }
  .front-card .claims { font-size: 13px; margin-top: 10px; line-height: 1.25; }

  .flavour-tag {
    position: absolute; left: 524px; top: 967px; width: 136px; height: 20px;
    background: var(--print-wrap);
    font-family: "Old Standard TT", serif; font-weight: 700; font-size: 11px;
    display: flex; align-items: center; justify-content: center; letter-spacing: 0.02em;
  }
  .volume {
    position: absolute; left: 524px; top: 990px; width: 136px; text-align: center;
    font-family: "Old Standard TT", serif; font-weight: 700; font-size: 12px;
  }

  /* Nutrition panel */
  .nutrition {
    position: absolute; left: 238px; top: 770px; width: 196px;
    background: var(--white); border: 1px solid #333;
    padding: 6px 7px; transform: rotate(-15deg); transform-origin: center;
    font-family: "Old Standard TT", serif; font-size: 7px; color: var(--ink); line-height: 1.15;
  }
  .nutrition h3 { font-size: 8px; font-weight: 700; border-bottom: 1px solid #333; padding-bottom: 2px; }
  .nutrition table { width: 100%; border-collapse: collapse; }
  .nutrition th { font-weight: 400; text-align: left; vertical-align: bottom; padding: 2px 0; border-bottom: 1px solid #333; }
  .nutrition td { padding: 0.5px 0; }
  .nutrition .num { text-align: right; }
  .nutrition .note { border-top: 1px solid #333; margin-top: 3px; padding-top: 3px; }

  /* Ingredients panel */
  .info {
    position: absolute; left: 800px; top: 742px; width: 178px;
    background: rgba(238, 248, 196, 0.85);
    transform: rotate(15deg); transform-origin: center;
    font-family: "Old Standard TT", serif; font-size: 9px; color: var(--ink);
    text-align: center; line-height: 1.15; padding: 6px 4px;
  }
  .info h3 { font-size: 9px; font-weight: 400; margin-bottom: 6px; }
  .info p { margin-bottom: 8px; }
  .company {
    position: absolute; left: 800px; top: 948px;
    transform: rotate(15deg);
    font-family: "Old Standard TT", serif; font-weight: 700; font-size: 12px;
  }
</style>
</head>
<body>
<svg class="artwork" viewBox="0 0 1200 1200" xmlns="http://www.w3.org/2000/svg">
  <defs>
    <clipPath id="wrap-shape">
      <path d="M164,728 Q600,616 1036,728 L948,1060 Q600,990 228,1060 Z"/>
    </clipPath>
  </defs>
  <!-- Lid -->
  <circle cx="600" cy="328" r="304" fill="var(--leaf)"/>
  <circle cx="600" cy="328" r="240" fill="var(--print-lid)" role="img" aria-label="Repeating avocado print"/>
  <!-- Side wrap -->
  <path d="M164,728 Q600,616 1036,728 L948,1060 Q600,990 228,1060 Z" fill="var(--print-wrap)" role="img" aria-label="Repeating avocado print"/>
  <path d="M432,600 L760,600 L708,1100 L480,1100 Z" fill="var(--leaf)" clip-path="url(#wrap-shape)"/>
</svg>

<section class="label-card lid-card">
  <h1 class="product-title">COCONUT AND AVOCADO<br>ICE CREAM</h1>
  <div class="rule"></div>
  <div class="brand"><span>GLENMORROW</span><span class="brand-dot"></span></div>
  <p class="tagline">Happiness is Avocado</p>
  <div class="rule lower"></div>
  <p class="claims">•vegan•dairy free•gluten free•<br>• refined sugar free•<br>•frozen desert•</p>
</section>

<div class="front-frame"></div>
<section class="label-card front-card">
  <h2 class="product-title">COCONUT AND AVOCADO<br>ICE CREAM</h2>
  <div class="brand"><span>GLENMORROW</span><span class="brand-dot"></span></div>
  <p class="tagline">Happiness is Avocado</p>
  <p class="claims">•vegan•dairy free•gluten free•<br>• refined sugar free•<br>•frozen desert•</p>
</section>
<div class="flavour-tag">ORIGINAL AVOCADO</div>
<div class="volume">500 ml ℮</div>

<aside class="nutrition">
  <h3>Nutrition</h3>
  <table>
    <tr><th>Typical values</th><th>100ml<br>contains</th><th>%<br>RI*</th><th class="num">RI* for an<br>average adult</th></tr>
    <tr><td>Energy</td><td>kJ<br>kcal</td><td>%</td><td class="num">8400kJ<br>2000kcal</td></tr>
    <tr><td>Fat</td><td>g</td><td>%</td><td class="num">70g</td></tr>
    <tr><td>of which saturates</td><td>g</td><td>%</td><td class="num">20g</td></tr>
    <tr><td>Carbohydrate</td><td>g</td><td>%</td><td class="num">260g</td></tr>
    <tr><td>of which sugars</td><td>g</td><td>%</td><td class="num">90g</td></tr>
    <tr><td>Fibre</td><td>g</td><td></td><td class="num"></td></tr>
    <tr><td>Protein</td><td>g</td><td>%</td><td class="num">50g</td></tr>
    <tr><td>Salt</td><td>g</td><td>%</td><td class="num">6g</td></tr>
  </table>
  <p class="note">This pack contains &nbsp;&nbsp;&nbsp;&nbsp; servings</p>
  <p>*Reference intake of an average adult (8400kJ / 2000kcal)</p>
</aside>

<aside class="info">
  <h3>INGRIDIENTS:</h3>
  <p>Coconut milk, Avocados, Agave syrup, Lime juice, Arrowroot, Guar gum, Xanthan gum, Salt.</p>
  <p>Made from coconut flesh and creamy avocado our ice cream offers an indulcent dairy free treat.</p>
  <p>For Best Before see base. Storage conditions - keep frozen -18 o C. Best removed from freezer 5 minutes before serving.</p>
</aside>
<div class="company">Glenmorrow LTD</div>
</body>
</html>
```